Cocktail-Making Assistant App re-design

Ok boys and girls, here's the deal:
I have an android app which is almost complete, but needs a design overhaul.

The app is a standard cocktail-making assistant: gives you a list of cocktails and the ability to see which cocktail you can make out of those ingredients (drinks, fruit, etc) you have at home.

I've attached some general app flow, as well as detailed requirements/explanation presentation. Most of those things are just FYI, so that you know what it's about.

3 screens are the most important (main screen, cocktail view screen, ingredient view screen), meaning I will pick the design mostly based on ideas for those 3 things, with the fourth being a rather simple list (given on attached flow, third tier)
Some other screens are derived from that, with some minor changes on it, but you shouldn't care about that.

There are lots of other, non-explained things which I said nothing about only because they are (from design point of view) completely the same and would only make it seem more complicated.

I don't want to influence the colour scheme, but the app will be released under RedCedar developer name (having a light colured red cedar as a logo) so I suppose some brownish design, for example, will not really fit nicely. If you, however, have a killer which you are confident will prove me wrong, I'm looking forward to seeing it!

It should be a serious, elegant look (as opposed to cartoonish, but we are not aiming for a business look at all!), not cluttered with details, no clubbing themes, glitter and so on.

Test apk file available on request (Android 2.3+).

Edit: payment is now guaranteed
Also please note that currently, the favorite, "heart" button has a motion effect:
on click it flies out of the screen to the left (white heart) and comes back to the screen as a red heart. Take that into consideration, if it means anything to you.

Reason: Some designers are enthusiastic but will need an extra weekend to polish their ideas.

Target Market(s)

Whoever you imagine would enjoy drinking cocktails

Industry/Entity Type

Business

Requirements
Must have
• Everything is said in the provided documentation - images say more than I could possibly write here.
Nice to have
• As said, most of the icons are a nice-to-have. Only those which are critically linked to the rest of the design must be provided. More details in the docs.
Should not have
• No cartoon look, No zillion colours

```html
<!DOCTYPE html>
<html lang="en">
<head>
<meta charset="utf-8">
<title>151 Florida Bushwacker</title>
<link href="https://fonts.googleapis.com/css2?family=Michroma&display=swap" rel="stylesheet">
<style>
:root{
  --ink:#1c1c1c;
  --accent-red:#e4242f;
  --header-bg:#f7f7f7;
  --info-bg:#f4f4f4;
  --footer-bg:#efefef;
  --muted:#555;
  --divider:#d8d8d8;
  --green:#add677;
  --orange:#fbb862;
  --red:#fd5e66;
  --taupe:#cfafa5;
  --yellow:#fee57a;
  --violet:#b2a8e6;
  --drinks-a:#f5a623;
  --drinks-b:#7fb23a;
}
*{margin:0;padding:0;box-sizing:border-box}
html,body{width:676px;height:1200px;overflow:hidden;background:#fff}
body{font-family:"Michroma",sans-serif;color:var(--ink);text-transform:uppercase}
.screen{position:relative;width:676px;height:1200px;overflow:hidden}

.app-header{position:absolute;left:0;top:0;width:676px;height:97px;background:linear-gradient(#fff,var(--header-bg))}
.app-header .divider{position:absolute;top:14px;width:1px;height:72px;background:var(--divider)}
.back-home{position:absolute;left:8px;top:22px}
.title{position:absolute;left:151px;top:17px;font-size:31px;line-height:32px;letter-spacing:1.5px;font-weight:400;-webkit-text-stroke:0.8px var(--ink)}
.camera{position:absolute;left:566px;top:26px}
.header-rule{position:absolute;left:0;top:97px;width:676px;height:9px;background:linear-gradient(var(--accent-red),#b5121b)}

.info{position:absolute;left:0;top:106px;width:676px;height:169px;background:var(--info-bg)}
.drinks-photo{position:absolute;left:4px;top:14px;width:154px;height:116px;border-radius:10px;background:radial-gradient(circle at 40% 55%,var(--drinks-a),var(--drinks-b) 70%,var(--info-bg) 100%)}
.rating{position:absolute;left:270px;top:34px;display:flex;gap:6px}
.rating-rule{position:absolute;left:178px;top:66px;width:392px;height:1px;background:#cfcfcf}
.volume{position:absolute;left:169px;top:70px;font-size:28px;letter-spacing:2px;-webkit-text-stroke:0.6px var(--ink)}
.favorite{position:absolute;left:572px;top:42px}

.ingredients{position:absolute;left:0;top:275px;width:676px;list-style:none}
.ingredient{position:relative;height:137.2px}
.ingredient .star{position:absolute;left:28px;top:50px}
.ingredient .name{position:absolute;left:101px;top:51px;font-size:27px;line-height:32px;letter-spacing:1.5px;-webkit-text-stroke:0.7px var(--ink)}
.ingredient .name.two-line{top:38px}
.ingredient .brand{display:block;color:#fff;-webkit-text-stroke:0.6px #fff;font-size:24px;line-height:32px;margin-top:10px}
.ingredient .cart{position:absolute;left:570px;top:24px}
.green{background:var(--green)}.orange{background:var(--orange)}.red{background:var(--red)}
.taupe{background:var(--taupe)}.yellow{background:var(--yellow)}.violet{background:var(--violet)}

.pull-footer{position:absolute;left:0;top:1098px;width:676px;height:102px;background:linear-gradient(#f8f8f8,var(--footer-bg))}
.pull-footer p{position:absolute;left:53px;top:33px;font-size:13.5px;letter-spacing:1px;color:var(--muted)}
.pull-footer .arrow{position:absolute;left:307px;top:62px}
.pull-footer .notch{position:absolute;left:306px;top:88px}
</style>
</head>
<body>
<div class="screen">
  <svg width="0" height="0" style="position:absolute">
    <defs>
      <symbol id="cart" viewBox="0 0 96 84">
        <path d="M4 14h14l12 46h48" fill="none" stroke="#1c1c1c" stroke-width="8" stroke-linecap="round" stroke-linejoin="round"/>
        <path d="M22 24h66l-10 28H30" fill="none" stroke="#1c1c1c" stroke-width="7" stroke-linejoin="round"/>
        <rect x="52" y="4" width="12" height="34" rx="4" transform="rotate(25 58 21)" fill="#1c1c1c"/>
        <rect x="66" y="0" width="10" height="10" transform="rotate(25 71 5)" fill="#1c1c1c"/>
        <circle cx="36" cy="74" r="7" fill="#1c1c1c"/>
        <circle cx="72" cy="74" r="7" fill="#1c1c1c"/>
      </symbol>
      <symbol id="star" viewBox="0 0 24 24">
        <path d="M12 1l3.2 7.4 8 .7-6 5.3 1.8 7.9L12 18.2 5 22.3l1.8-7.9-6-5.3 8-.7z"/>
      </symbol>
    </defs>
  </svg>

  <header class="app-header">
    <svg class="back-home" width="80" height="56" viewBox="0 0 80 56" aria-label="Home">
      <path d="M12 18l-9 10 9 10" fill="none" stroke="var(--accent-red)" stroke-width="3"/>
      <path d="M48 4L20 28h8v22h14V36h12v14h14V28h8z" fill="#1c1c1c"/>
    </svg>
    <span class="divider" style="left:131px"></span>
    <h1 class="title">151 Florida<br>Bushwacker</h1>
    <span class="divider" style="left:545px"></span>
    <svg class="camera" width="68" height="50" viewBox="0 0 68 50" aria-label="Camera">
      <path d="M6 10h14l5-8h18l5 8h14a4 4 0 0 1 4 4v30a4 4 0 0 1-4 4H6a4 4 0 0 1-4-4V14a4 4 0 0 1 4-4z" fill="#1c1c1c"/>
      <circle cx="34" cy="29" r="13" fill="#fff"/>
      <circle cx="34" cy="29" r="8" fill="#1c1c1c"/>
      <rect x="8" y="14" width="8" height="4" fill="#fff"/>
    </svg>
  </header>
  <div class="header-rule"></div>

  <section class="info">
    <div class="drinks-photo" role="img" aria-label="Photo of assorted cocktails with citrus and mint"></div>
    <div class="rating">
      <svg width="32" height="32" fill="var(--green)"><use href="#star"/></svg>
      <svg width="32" height="32" fill="var(--orange)"><use href="#star"/></svg>
      <svg width="32" height="32" fill="var(--red)"><use href="#star"/></svg>
      <svg width="32" height="32" fill="var(--violet)"><use href="#star"/></svg>
      <svg width="32" height="32" fill="var(--taupe)"><use href="#star"/></svg>
    </div>
    <div class="rating-rule"></div>
    <p class="volume">Vol unavailable</p>
    <svg class="favorite" width="96" height="80" viewBox="0 0 96 80" aria-label="Add to favourites">
      <path d="M36 72L8 44A18 18 0 0 1 36 18a18 18 0 0 1 28 26z" fill="#333"/>
      <circle cx="68" cy="54" r="20" fill="#333" stroke="var(--info-bg)" stroke-width="4"/>
      <path d="M68 43v22M57 54h22" stroke="#fff" stroke-width="5"/>
    </svg>
  </section>

  <ul class="ingredients">
    <li class="ingredient green">
      <svg class="star" width="30" height="30" fill="#333"><use href="#star"/></svg>
      <span class="name">1/2 oz Corala rum</span>
      <svg class="cart" width="96" height="84" aria-label="In stock"><use href="#cart"/><circle cx="14" cy="34" r="10" fill="#333"/><path d="M9 34l4 4 6-7" fill="none" stroke="#fff" stroke-width="2.5"/></svg>
    </li>
    <li class="ingredient orange">
      <svg class="star" width="30" height="30" fill="#333"><use href="#star"/></svg>
      <span class="name">1/2 oz light rum</span>
      <svg class="cart" width="96" height="84" aria-label="Add to shopping list"><use href="#cart"/><circle cx="14" cy="34" r="10" fill="#333"/><path d="M14 28v12M8 34h12" stroke="#fff" stroke-width="2.5"/></svg>
    </li>
    <li class="ingredient red">
      <svg class="star" width="30" height="30" fill="#333"><use href="#star"/></svg>
      <span class="name two-line">1 oz 151 proof rum<span class="brand">Seaward</span></span>
      <svg class="cart" width="96" height="84" aria-label="Add to shopping list"><use href="#cart"/><circle cx="14" cy="34" r="10" fill="#333"/><path d="M14 28v12M8 34h12" stroke="#fff" stroke-width="2.5"/></svg>
    </li>
    <li class="ingredient taupe">
      <svg class="star" width="30" height="30" fill="#333"><use href="#star"/></svg>
      <span class="name two-line">1 oz dark creme<br>de cacao</span>
      <svg class="cart" width="96" height="84" aria-label="In stock"><use href="#cart"/><circle cx="14" cy="34" r="10" fill="#333"/><path d="M9 34l4 4 6-7" fill="none" stroke="#fff" stroke-width="2.5"/></svg>
    </li>
    <li class="ingredient yellow">
      <svg class="star" width="30" height="30" fill="#333"><use href="#star"/></svg>
      <span class="name">1 oz Vellandre</span>
      <svg class="cart" width="96" height="84" aria-label="Shopping cart"><use href="#cart"/></svg>
    </li>
    <li class="ingredient violet">
      <svg class="star" width="30" height="30" fill="#333"><use href="#star"/></svg>
      <span class="name">1 oz milk</span>
      <svg class="cart" width="96" height="84" aria-label="Shopping cart"><use href="#cart"/></svg>
    </li>
  </ul>

  <footer class="pull-footer">
    <p>Pull up to view details about making this cocktail.</p>
    <svg class="arrow" width="20" height="20" viewBox="0 0 20 20"><path d="M10 18V3M4 9l6-6 6 6" fill="none" stroke="var(--muted)" stroke-width="2.5"/></svg>
    <svg class="notch" width="24" height="14" viewBox="0 0 24 14"><path d="M0 14L12 2l12 12z" fill="#fff" stroke="#ddd"/></svg>
  </footer>
</div>
</body>
</html>
```